QTV Advisory needs business card

Having just developed a logo, I now want to use that logo in the development of a business card. The card should contain the logo, my name, title, phone, email, website and physical address. I would like to use one side of the card for details and the other side for logo and messaging. Use your creativity to place the information effectively. I want the logo to appear in a strong blue, which may be matched on the back side of the card, where the logo might be reversed out in white. I want the text to be in either dark blue or black (not light blue or gray).
I am consultant, primarily helping small and mid-size companies refine their strategy, reorganize their staff and propel forward in their industry. I also teach at universities and coach on a one-on-one basis. The final design should reflect expertise, guidance, judgement, perspective, experience.
The font used in the logo is ACaslonPro.

Target Market(s)

small to mid-size companies in the US seeking business guidance

Industry/Entity Type

Business

Font styles to use
Other font styles liked:
• ACaslonPro

Colors
0455a3
0255a3
3277b5

Requirements
Must have
• Card must convey my name and information clearly. Do not make it too small - many of my customers are 50+ years old. Please use all three of my titles: consultant / coach / instructor.
Should not have
• Please do not use icons to represent the phone, email, web. Do not use p / e / w either to indicate those details.

I have decided that a swatch of color, especially a "blue wave," does not work for me. I would rather have a simpler, more reserved look rather than a very contemporary, high color card.

Please do not deconstruct the logo or put it in a different font or italics.

```html
<!DOCTYPE html>
<html lang="en">
<head>
<meta charset="utf-8">
<title>QTV Advisory – Business Card</title>
<link rel="stylesheet" href="https://fonts.googleapis.com/css2?family=Open+Sans:wght@400;600;700&display=swap">
<style>
  :root {
    --brand-blue: #0455a3;
    --accent-blue: #3277b5;
    --ink: #1c1c1c;
    --ink-soft: #3a3a3a;
    --paper: #ffffff;
    --card-dark: #1b1b1b;
    --card-dark-hi: #3a3a3a;
    --band-dark: #111111;
    --stage: #e9e7e4;
  }
  * { box-sizing: border-box; margin: 0; padding: 0; }
  html, body {
    width: 1200px; height: 800px; overflow: hidden;
    background: var(--stage);
    font-family: "Open Sans", Arial, sans-serif;
  }
  .stage {
    position: relative; width: 1200px; height: 800px;
    display: flex; align-items: center; justify-content: center; gap: 60px;
  }
  .card {
    position: relative; width: 520px; height: 297px; overflow: hidden;
    box-shadow: 0 6px 18px rgba(0,0,0,0.18);
  }

  /* Back side */
  .card-back {
    background: linear-gradient(135deg, var(--card-dark-hi) 0%, var(--card-dark) 55%, #0e0e0e 100%);
  }
  .card-back .rail {
    position: absolute; top: 0; bottom: 0; width: 14px;
    background: rgba(0,0,0,0.55);
  }
  .card-back .rail-left { left: 88px; }
  .card-back .rail-right { right: 88px; }
  .card-back .brand {
    position: absolute; inset: 0;
    display: flex; align-items: center; justify-content: center; gap: 14px;
  }
  .brand-mark { width: 30px; height: 30px; }
  .card-back .brand-name {
    color: var(--paper); font-weight: 600; font-size: 30px; letter-spacing: 3px;
  }

  /* Front side */
  .card-front { background: var(--paper); }
  .card-front .brand {
    position: absolute; top: 26px; right: 34px;
    display: flex; align-items: center; gap: 10px;
  }
  .card-front .brand-mark { width: 24px; height: 24px; }
  .card-front .brand-name {
    color: var(--brand-blue); font-weight: 600; font-size: 24px; letter-spacing: 2px;
  }
  .address {
    position: absolute; top: 96px; left: 30px;
    font-size: 12px; line-height: 1.45; color: var(--ink-soft);
  }
  .person {
    position: absolute; top: 130px; left: 220px;
  }
  .person-name {
    color: var(--brand-blue); font-weight: 700; font-size: 18px;
  }
  .person-titles {
    color: var(--ink); font-size: 14px; margin-top: 2px;
  }
  .contact {
    margin-top: 14px; display: grid; grid-template-columns: 56px auto;
    row-gap: 2px; font-size: 14px;
  }
  .contact dt { color: var(--accent-blue); font-weight: 600; }
  .contact dd { color: var(--ink); }
  .footer-band {
    position: absolute; left: 0; right: 0; bottom: 0; height: 40px;
    background: var(--band-dark);
    border-top: 3px solid var(--accent-blue);
    box-shadow: 0 -5px 0 var(--paper), 0 -7px 0 var(--accent-blue);
    display: flex; align-items: center; padding-left: 30px;
  }
  .website {
    color: var(--paper); font-weight: 700; font-size: 15px; letter-spacing: 0.3px;
  }
</style>
</head>
<body>
<main class="stage">
  <section class="card card-back" aria-label="Card back">
    <div class="rail rail-left"></div>
    <div class="rail rail-right"></div>
    <div class="brand">
      <svg class="brand-mark" viewBox="0 0 30 30" aria-hidden="true"><rect width="30" height="30" fill="#ffffff"/></svg>
      <span class="brand-name">QTV ADVISORY</span>
    </div>
  </section>

  <section class="card card-front" aria-label="Card front">
    <div class="brand">
      <svg class="brand-mark" viewBox="0 0 24 24" aria-hidden="true"><rect width="24" height="24" fill="#0455a3"/></svg>
      <span class="brand-name">QTV ADVISORY</span>
    </div>

    <address class="address">
      2217 Larkspur Court<br>
      Tampa, FL 33602
    </address>

    <div class="person">
      <p class="person-name">R. Dalton Whitmore, CCIM</p>
      <p class="person-titles">Consultant | Coach | Instructor</p>
      <dl class="contact">
        <dt>Phone:</dt><dd>(555) 014-2290</dd>
        <dt>Email:</dt><dd>Dalton@qtv-advisory.com</dd>
      </dl>
    </div>

    <div class="footer-band">
      <span class="website">www.qtv-advisory.com</span>
    </div>
  </section>
</main>
</body>
</html>
```